International wholesale business needs a business card

We need a business card.

Company Details:
Company Name and logo
Address, Phone number, Website
Employee Details:
Name, Designation, Mobile Number & Email address

Logo file is attached.

```html
<!DOCTYPE html>
<html lang="en">
<head>
<meta charset="utf-8">
<title>Korvane Trading – Business Card</title>
<link rel="stylesheet" href="https://fonts.googleapis.com/css2?family=Montserrat:wght@400;500;700&display=swap">
<style>
  :root {
    --stage: #2b2b2d;
    --card-grey: #8b9196;
    --brand-red: #c1272d;
    --paper-white: #ffffff;
    --ink: #1c1c1c;
  }
  * { box-sizing: border-box; margin: 0; padding: 0; }
  html, body { width: 1200px; height: 1015px; overflow: hidden; }
  body {
    background: var(--stage);
    font-family: "Montserrat", sans-serif;
    display: flex;
    flex-direction: column;
    align-items: center;
    justify-content: center;
    gap: 60px;
  }
  .card {
    position: relative;
    width: 720px;
    height: 411px;
    background: var(--card-grey);
    overflow: hidden;
    box-shadow: 0 10px 30px rgba(0,0,0,.5);
  }

  /* Back */
  .card-back .brand {
    position: absolute;
    left: 46px;
    bottom: 46px;
  }

  /* Brand lockup */
  .brand {
    display: flex;
    align-items: center;
    gap: 14px;
  }
  .brand-dot {
    width: 46px;
    height: 46px;
    border-radius: 50%;
    background: var(--brand-red);
    flex: none;
  }
  .brand-name {
    color: var(--brand-red);
    font-weight: 700;
    font-size: 34px;
    letter-spacing: 2px;
    line-height: 1;
  }

  /* Front */
  .card-front .brand {
    position: absolute;
    left: 150px;
    top: 58px;
  }
  .info-band {
    position: absolute;
    left: 0; right: 0;
    top: 168px;
    height: 146px;
    background: var(--brand-red);
    display: flex;
    align-items: center;
    justify-content: center;
    gap: 26px;
    color: var(--paper-white);
  }
  .person { text-align: right; }
  .person-name {
    font-weight: 700;
    font-size: 27px;
    letter-spacing: .5px;
    line-height: 1.05;
  }
  .person-role {
    font-weight: 500;
    font-size: 18px;
    line-height: 1.2;
  }
  .divider {
    width: 2px;
    height: 104px;
    background: var(--paper-white);
  }
  .contacts { list-style: none; }
  .contacts li {
    display: flex;
    align-items: center;
    gap: 10px;
    font-size: 17px;
    line-height: 26px;
  }
  .contacts svg { width: 18px; height: 18px; flex: none; }

  .address-strip {
    position: absolute;
    left: 0; right: 0;
    top: 314px;
    height: 72px;
    background: var(--paper-white);
    display: flex;
    align-items: center;
    justify-content: center;
    color: var(--ink);
    font-size: 20px;
  }
  .accent-stripe {
    position: absolute;
    left: 0; right: 0; bottom: 0;
    height: 25px;
    display: flex;
  }
  .accent-stripe .grey { flex: 1; background: var(--card-grey); }
  .accent-stripe .red { flex: 1; background: var(--brand-red); }
</style>
</head>
<body>

  <section class="card card-back" aria-label="Card back">
    <div class="brand">
      <span class="brand-dot"></span>
      <span class="brand-name">KORVANE TRADING</span>
    </div>
  </section>

  <section class="card card-front" aria-label="Card front">
    <div class="brand">
      <span class="brand-dot"></span>
      <span class="brand-name">KORVANE TRADING</span>
    </div>

    <div class="info-band">
      <div class="person">
        <p class="person-name">DANIEL REYES</p>
        <p class="person-role">Managing Director</p>
      </div>
      <span class="divider"></span>
      <ul class="contacts">
        <li>
          <svg viewBox="0 0 24 24" fill="none" stroke="#fff" stroke-width="2.2"><path d="M5 3h4l2 5-2.5 1.5a11 11 0 0 0 6 6L16 13l5 2v4a2 2 0 0 1-2 2A17 17 0 0 1 3 5a2 2 0 0 1 2-2z"/></svg>
          044-987 654 321
        </li>
        <li>
          <svg viewBox="0 0 24 24" fill="none" stroke="#fff" stroke-width="2.2"><rect x="6" y="2" width="12" height="20" rx="2"/><line x1="11" y1="18" x2="13" y2="18"/></svg>
          044-987 654 321
        </li>
        <li>
          <svg viewBox="0 0 24 24" fill="none" stroke="#fff" stroke-width="2.2"><rect x="2" y="5" width="20" height="14"/><path d="M2 5l10 8 10-8"/></svg>
          info@korvanetrade.com
        </li>
        <li>
          <svg viewBox="0 0 24 24" fill="none" stroke="#fff" stroke-width="2"><circle cx="12" cy="12" r="10"/><ellipse cx="12" cy="12" rx="4" ry="10"/><line x1="2" y1="12" x2="22" y2="12"/></svg>
          www.korvanetrade.com
        </li>
      </ul>
    </div>

    <div class="address-strip">
      <p>38, Harbour Road, Suite 5 10234, Portland</p>
    </div>

    <div class="accent-stripe">
      <span class="grey"></span>
      <span class="red"></span>
    </div>
  </section>

</body>
</html>
```